Snuggle Stitch Needs a Beautiful Website

I need a new website for this new E-commerce. I sell handmade baby crochets, e.g. booties, headbands, hats, etc. I need a feminine and soft design to make the moms-to-be say 'oohh ahh'. I'd like pink, blue and gray. I'd like an inviting homepage, and nice regular pages where people can see and order the products.

Industry/Entity Type

Baby

Requirements
Must have
• beautiful, soft, feminine design. Please use pictures of the colors I'd like: brown, yellow, pink and blue. Any combination, but definitely include brown.

```html
<!DOCTYPE html>
<html lang="en">
<head>
<meta charset="utf-8">
<title>Snuggle Stitch – Handmade Baby Crochets</title>
<link rel="stylesheet" href="https://fonts.googleapis.com/css2?family=Noto+Serif:ital,wght@0,400;0,700;1,400;1,700&family=PT+Sans:wght@400;700&display=swap">
<style>
:root{
  --pink:#e8307f;
  --pink-dark:#c91e68;
  --blue:#14a6d2;
  --blue-dark:#0a8dbb;
  --gray-text:#444;
  --light:#f3f3f3;
  --border:#dcdcdc;
  --white:#fff;
}
*{margin:0;padding:0;box-sizing:border-box}
html,body{width:1170px;height:1200px;overflow:hidden}
body{
  position:relative;
  font-family:"PT Sans",sans-serif;
  color:var(--gray-text);
  background:linear-gradient(160deg,#7fb4c9 0%,#c7d8c8 30%,#d8b6cc 55%,#a86aaa 80%,#6f5aa4 100%);
}
.abs{position:absolute}
.page{left:212px;top:0;width:748px;height:1060px;background:var(--white);box-shadow:0 0 10px rgba(0,0,0,.15)}
.brand{left:240px;top:22px;display:flex;align-items:center;gap:6px;font-family:"Noto Serif",serif;font-weight:700;font-size:25px;color:var(--pink)}
.brand-dot{width:12px;height:12px;border-radius:50%;background:var(--blue)}
.cart{left:744px;top:19px;width:204px;height:26px;border:1px solid var(--border);box-shadow:0 1px 2px rgba(0,0,0,.15);font-size:8.5px;display:flex;align-items:center;justify-content:space-between;padding:0 24px 0 20px;color:#111}
.cart em{font-style:normal;color:var(--pink)}
.cart a{color:var(--blue);text-decoration:none}
.nav{left:224px;top:70px;width:724px;height:31px;background:var(--pink)}
.nav a{position:absolute;top:0;height:31px;line-height:31px;font-family:"Noto Serif",serif;font-style:italic;font-weight:700;font-size:11.5px;color:var(--white);text-decoration:none}
.nav .active{left:0;width:61px;background:var(--blue);text-align:center}
.search{left:532px;top:6px;width:180px;height:20px;background:var(--white);border-radius:10px;box-shadow:inset 0 1px 2px rgba(0,0,0,.3);font-size:9px;color:#999;line-height:20px;padding-left:10px;font-style:italic}
.search b{position:absolute;right:2px;top:2px;width:28px;height:16px;border-radius:8px;background:#e4e4e4;color:#333;font-style:normal;font-size:9px;line-height:16px;text-align:center}
.hero{left:225px;top:114px;width:722px;height:242px;border-radius:3px;overflow:hidden;background:linear-gradient(100deg,#2b1a12 0%,#6b4520 35%,#8f6b5c 60%,#b38aa4 100%)}
.hero-photo{right:0;top:0;width:340px;height:242px;background:linear-gradient(160deg,#8e8f9a 0%,#a9a6b2 50%,#c59ab4 100%)}
.hero h1{left:31px;top:22px;font-family:"Noto Serif",serif;font-style:italic;font-weight:700;font-size:42px;color:var(--pink)}
.hero h2{left:31px;top:86px;font-family:"Noto Serif",serif;font-weight:400;font-size:15px;color:var(--white);letter-spacing:.2px}
.hero p{left:32px;top:116px;width:300px;font-size:11.3px;line-height:17.6px;color:var(--white)}
.btn-shop{left:31px;top:187px;width:92px;height:28px;border-radius:3px;background:var(--blue);color:var(--white);font-family:"Noto Serif",serif;font-style:italic;font-weight:700;font-size:13px;text-align:center;line-height:28px;box-shadow:0 1px 2px rgba(0,0,0,.4)}
.dots{left:670px;top:223px;display:flex;gap:4px}
.dots i{width:6px;height:6px;border-radius:50%;background:var(--white)}
.dots i:first-child{background:var(--pink)}
.side-box{left:225px;width:133px;background:linear-gradient(#fff,#ececec);border:1px solid #e2e2e2;border-radius:2px}
.side-box h3{position:absolute;left:9px;top:9px;font-family:"Noto Serif",serif;font-style:italic;font-weight:700;font-size:10.5px;color:#444}
.side-box li{position:absolute;list-style:none;font-size:8.6px;color:#333}
.side-box .more{color:var(--blue)}
.promo{left:225px;top:650px;width:133px;height:166px;border-radius:2px;overflow:hidden}
.promo-photo{left:0;top:0;width:133px;height:130px;background:linear-gradient(160deg,#cfe0ec 0%,#e9d2c5 60%,#f2f2f2 100%)}
.promo-band{left:0;top:130px;width:133px;height:36px;background:var(--pink);color:var(--white);font-family:"Noto Serif",serif;font-style:italic;font-size:13px;line-height:36px;text-align:center}
.section-bar{left:370px;width:578px;height:25px;background:linear-gradient(var(--blue),var(--blue-dark));border-radius:2px 2px 0 0;color:var(--white);font-family:"Noto Serif",serif;font-weight:700;font-size:11.5px;line-height:25px;padding-left:10px;border-bottom:3px solid #0a7ea8}
.card{width:136px;height:172px;border:1px solid var(--border);background:var(--white)}
.card .label{position:absolute;left:9px;top:6px;font-size:8.6px;color:var(--blue)}
.card .thumb{position:absolute;left:8px;top:21px;width:120px;height:120px}
.card .price{position:absolute;left:6px;top:151px;font-family:"Noto Serif",serif;font-weight:700;font-size:10.5px;color:#111}
.card .buy{position:absolute;right:7px;top:148px;width:64px;height:19px;border-radius:3px;background:var(--pink);color:var(--white);font-family:"Noto Serif",serif;font-style:italic;font-weight:700;font-size:9.5px;line-height:19px;text-align:center;box-shadow:0 1px 2px rgba(0,0,0,.3)}
.welcome-title{left:374px;top:840px;font-family:"Noto Serif",serif;font-weight:700;font-size:12px;color:var(--blue)}
.welcome-photo{left:374px;top:872px;width:149px;height:106px;background:linear-gradient(135deg,#b54a3a 0%,#5d6670 40%,#d9b86a 70%,#2d4a5a 100%)}
.welcome-text{left:534px;top:868px;width:404px;font-size:9.2px;line-height:16px;text-align:justify;color:#333}
.footer{left:224px;top:1016px;width:724px;height:28px;background:var(--pink)}
.footer nav{position:absolute;left:22px;top:0;line-height:28px;font-family:"Noto Serif",serif;font-style:italic;font-weight:700;font-size:9.5px;color:var(--white)}
.footer nav span{margin:0 5px;font-style:normal;font-weight:400}
.social{right:40px;top:9px;display:flex;gap:9px}
.social i{width:10px;height:10px;border-radius:50%;background:var(--white)}
.snow{left:0;top:1072px;width:1170px;height:128px;background:linear-gradient(rgba(255,255,255,0) 0%,rgba(255,255,255,.6) 55%,#fff 100%)}
</style>
</head>
<body>
<div class="abs page"></div>

<div class="abs brand"><span class="brand-dot"></span>Snuggle Stitch</div>
<div class="abs cart"><span>Shopping Cart: <em>0 items</em></span><a>View cart</a></div>

<div class="abs nav">
  <a class="active">Home</a>
  <a style="left:78px">About Us</a>
  <a style="left:161px">New Arrials</a>
  <a style="left:270px">Baby Crochets</a>
  <a style="left:383px">Blog</a>
  <a style="left:438px">Contact</a>
  <div class="abs search">Search<b>GO</b></div>
</div>

<section class="abs hero">
  <div class="abs hero-photo" role="img" aria-label="Expecting mother holding pink and blue crocheted baby booties"></div>
  <h1 class="abs">New Arrials</h1>
  <h2 class="abs">DOLOR SIT AMET, CONSECTETUR ADIPISCING ELIT.</h2>
  <p class="abs">Ut metus felis, posuere ac eleifend eget, tristique id magna. In iaculis pellentesque nisl vel blandit. Phasellus ac orci eget mi malesuada varius ac quis purus.</p>
  <div class="abs btn-shop">Shop Now</div>
  <div class="abs dots"><i></i><i></i><i></i><i></i></div>
</section>

<aside>
  <div class="abs side-box" style="top:370px;height:146px">
    <h3>Shop by Category</h3>
    <ul>
      <li style="left:13px;top:35px">Crochets</li>
      <li style="left:13px;top:53px">Booties</li>
      <li style="left:13px;top:71px">Headbands,</li>
      <li style="left:13px;top:88px">Hats</li>
      <li class="more" style="left:13px;top:106px">More</li>
    </ul>
  </div>
  <div class="abs side-box" style="top:528px;height:110px">
    <h3>Shop by Price</h3>
    <ul>
      <li style="left:19px;top:35px">Under $25</li>
      <li style="left:19px;top:52px">$25 - $50</li>
      <li style="left:19px;top:70px">$50 - $100</li>
      <li style="left:19px;top:88px">Over $100</li>
    </ul>
  </div>
  <div class="abs promo">
    <div class="abs promo-photo" role="img" aria-label="Sleeping newborn in a blue knitted hat"></div>
    <div class="abs promo-band">Exclusive Discount</div>
  </div>
</aside>

<div class="abs section-bar" style="top:370px">FEATURED PRODUCTS</div>
<div class="abs card" style="left:370px;top:406px"><span class="label">Product #001</span><div class="thumb" role="img" aria-label="Pink crochet crown headband" style="background:linear-gradient(#f6f6f6,#f3a9c8 60%,#eeeeee)"></div><span class="price">$78.88</span><span class="buy">Buy Now</span></div>
<div class="abs card" style="left:518px;top:406px"><span class="label">Product #002</span><div class="thumb" role="img" aria-label="Pale pink crochet ballet booties with rosettes" style="background:linear-gradient(#f0d6e0,#e9b8c8 60%,#ddd8d2)"></div><span class="price">$18.88</span><span class="buy">Buy Now</span></div>
<div class="abs card" style="left:665px;top:406px"><span class="label">Product #003</span><div class="thumb" role="img" aria-label="Teal crochet booties with button strap" style="background:linear-gradient(#5a6e78,#2f98a8 60%,#7a8a90)"></div><span class="price">$24.88</span><span class="buy">Buy Now</span></div>
<div class="abs card" style="left:812px;top:406px"><span class="label">Product #004</span><div class="thumb" role="img" aria-label="Aqua crochet crown headband" style="background:linear-gradient(#f2f2f2,#6fd3e6 60%,#ececec)"></div><span class="price">$111.00</span><span class="buy">Buy Now</span></div>

<div class="abs section-bar" style="top:610px">OUR PRODUCTS</div>
<div class="abs card" style="left:370px;top:646px"><span class="label">Product #005</span><div class="thumb" role="img" aria-label="Gray crochet booties with red flower" style="background:linear-gradient(#8a8a8e,#6a6a70 60%,#9a9aa0)"></div><span class="price">$78.88</span><span class="buy">Buy Now</span></div>
<div class="abs card" style="left:518px;top:646px"><span class="label">Product #006</span><div class="thumb" role="img" aria-label="Red crochet booties with flower" style="background:linear-gradient(#b8b8bc,#b52028 60%,#a8a8ac)"></div><span class="price">$36.88</span><span class="buy">Buy Now</span></div>
<div class="abs card" style="left:665px;top:646px"><span class="label">Product #003</span><div class="thumb" role="img" aria-label="Bright pink crochet crown" style="background:linear-gradient(#f4f4f4,#ee86d0 60%,#f0f0f0)"></div><span class="price">$85.00</span><span class="buy">Buy Now</span></div>
<div class="abs card" style="left:812px;top:646px"><span class="label">Product #003</span><div class="thumb" role="img" aria-label="Brown crochet sneaker booties with pink star" style="background:linear-gradient(#8a4d80,#5a4638 55%,#e8e2dc)"></div><span class="price">$14.88</span><span class="buy">Buy Now</span></div>

<h2 class="abs welcome-title">WELCOME TO SNUGGLE STITCH</h2>
<div class="abs welcome-photo" role="img" aria-label="Grid of colorful crochet sneaker booties"></div>
<p class="abs welcome-text">Consectetur adipisicing elit, sed do eiusmod tempor incididunt ut labore et dolore magna aliqua. Ut enim ad minim veniam, quis nostrud exercitation ullamco laboris nisi ut aliquip ex ea commodo consequat. Duis aute irure dolor in reprehenderit in voluptate velit esse cillum dolore eu fugiat nulla pariatur. Excepteur sint occaecat cupidatat non proident, sunt in culpa qui officia deserunt mollit anim id est laborum. Consectetur adipisicing elit, sed do eiusmod tempor incididunt ut labore et dolore magna aliqua. Ut enim ad minim veniam, quis nostrud exercitation ullamco laboris nisi ut aliquip ex ea commodo consequat. Duis aute irure dolor in reprehenderit in voluptate velit</p>

<footer class="abs footer">
  <nav>Home<span>|</span>About Us<span>|</span>New Arrials<span>|</span>Baby Crochets<span>|</span>Blog<span>|</span>Contact</nav>
  <div class="abs social"><i></i><i></i><i></i><i></i></div>
</footer>

<div class="abs snow" role="img" aria-label="Snowy winter landscape with cottage and pine trees"></div>
</body>
</html>
```